Marrowdale Institute Word Document Template

At the Marrowdale Institute, we want to offer our employees the ability to download branded word document templates that allow non-designers to create professional and on-brand documents. Through the use of theme preferences, locked elements and paragraph styles, the final deliverables should contain the brand elements identified at brand.mrwdl.edu including the primary logo, fonts, and colors.

GENERAL TEMPLATE
A multi-functional document that contains a range of styles and brand elements that can be used broadly. The template should be flexible enough to work as a single-page document, or a multi-page document.

Target Market(s)

Administrative staff and faculty (Non-designers) who create documents largely for internal use

Font styles to use
Sans Serif
Other font styles liked:
• Fonts are attached – Roboto should be used predominantly with Antonio and Zilla available to use when appropriate. Fonts should default to Arial if fonts are not installed.

Colors
fbed22
ffffff
000000

Requirements
Must have
• REQUIREMENTS:
Use brand assets at brand.mrwdl.edu (primary logo, fonts, colors are all available to download there).
If possible, fonts should default to Arial – if user does not have fonts installed.
Browse brand.mrwdl.edu to get a sense of the established look and feel.
No elements should bleed off the page.
The final deliverable should be as locked down as possible. The logo should not be editable.

ELEMENTS TO INCLUDE:
Masthead to include: Primary logo and Placeholder for Unit name
Paragraph styles:
Document Title
Subhead 1
Subhead 2
Body
Bullets
Photo Placeholder
Pull Quote
Caption
Footer to include statement (small): The Marrowdale Institute prohibits discrimination in employment, educational programs, and activities on the basis of race, creed, color, religion, national origin, age, sex, pregnancy, disability, genetic information, status as a U.S. veteran, service in the U.S. military, sexual orientation, gender identity, associational preferences, or any other classification that deprives the person of consideration as an individual. The university also affirms its commitment to providing equal opportunities and equal access to university facilities. For additional information on nondiscrimination policies, contact the Director, Bureau of Fair Access and Inclusion, the Marrowdale Institute, 418 Penwick Hall, Harlow Falls, MN 52279-4083, 319-482-6613 (voice), 319-482-6671 (TDD), inclusion@mrwdl.edu.
Nice to have
• Additional page templates for added flexibility would be nice...Such as a Cover sheet and/or Table of contents.

```html
<!DOCTYPE html>
<html lang="en">
<head>
<meta charset="utf-8">
<title>Marrowdale Institute Document Template</title>
<link href="https://fonts.googleapis.com/css2?family=Antonio:wght@400;700&family=Roboto:ital,wght@0,400;0,700;1,400&display=swap" rel="stylesheet">
<style>
:root{
  --gold:#fbd800;
  --black:#000;
  --white:#fff;
  --ink:#222;
  --muted:#888;
  --row:#f1f1f1;
  --placeholder:#e8eefa;
}
*{box-sizing:border-box;margin:0;padding:0}
html,body{width:1200px;height:2335px;overflow:hidden;background:var(--white)}
body{font-family:Roboto,Arial,sans-serif;color:var(--ink)}
.board{position:absolute;left:0;top:0;width:1324px;height:2577px;transform:scale(.9063);transform-origin:0 0}
.page{position:absolute;width:565px;height:731px;background:var(--white);box-shadow:0 14px 22px rgba(0,0,0,.22),0 0 3px rgba(0,0,0,.08)}
.abs{position:absolute}
.logo{position:absolute;font-family:Antonio,Arial,sans-serif;font-weight:700;letter-spacing:.5px;line-height:1;white-space:nowrap}
.logo.gold{color:var(--gold)}
.logo.black{color:var(--black)}
.doc-label{position:absolute;right:48px;top:30px;font-size:9px;color:var(--black)}
.display{font-family:Antonio,Arial,sans-serif;font-weight:700;color:var(--black);line-height:1;white-space:nowrap}
.photo{position:absolute}
.gold-band{position:absolute;background:var(--gold)}
.footer-rule{position:absolute;left:42px;width:479px;top:670px;height:2px;background:var(--gold)}
.footer-note{position:absolute;left:44px;top:677px;width:477px;font-size:4.6px;line-height:7.2px;color:var(--muted);text-align:justify}
.body p{font-size:9px;line-height:12.5px;margin-bottom:5px;text-align:justify;color:var(--ink)}
.toc-row{display:flex;align-items:baseline;font-size:10px;font-weight:700;color:var(--black);height:18px}
.toc-row .dots{flex:1;border-bottom:1.5px dotted #333;margin:0 3px;transform:translateY(-3px)}
.toc-row.sub{font-size:8.5px;font-weight:400;color:var(--muted)}
.toc-row.sub .dots{border-bottom:1px dashed #999}
.bullets{list-style:none;font-size:9px;color:var(--black)}
.bullets li{height:19.5px;display:flex;align-items:center;gap:8px}
.bullets .l2{padding-left:50px}
.tick{width:9px;height:9px;display:inline-flex}
.ring{width:5px;height:5px;border:1px solid #333;border-radius:50%;display:inline-block}
table{border-collapse:collapse;font-size:8px}
.t1{width:472px}
.t1 th{background:var(--gold);text-align:left;font-weight:700;color:var(--white);height:22px;padding-left:6px}
.t1 td{height:23px;padding-left:6px;border-bottom:1.5px solid #444}
.t1 tr:nth-child(odd) td{background:var(--row)}
.t2{width:378px}
.t2 th{background:var(--black);color:var(--white);text-align:left;height:24px;padding-left:6px;border-right:1px solid #fff}
.t2 td{height:24px;padding-left:6px;border:1px solid #ccc}
.t2 tr:nth-child(odd) td{background:var(--row)}
.t2 td:first-child{font-weight:700}
.caption{font-size:7.5px;font-style:italic;color:var(--black)}
</style>
</head>
<body>
<div class="board">

<!-- Cover -->
<section class="page cover" style="left:70px;top:98px">
  <div class="photo" role="img" aria-label="Photo of campus columns in front of a domed academic hall under a cloudy blue sky" style="left:20px;top:20px;width:524px;height:460px;background:linear-gradient(180deg,#2f62c9 0%,#8fa9d8 25%,#c9cfd6 45%,#7d7569 62%,#3c6a2e 78%,#4f9a35 100%)"></div>
  <div class="gold-band" style="left:20px;top:480px;width:524px;height:230px"></div>
  <h1 class="display abs" style="left:62px;top:497px;font-size:54px;letter-spacing:-.3px">DOCUMENT TITLE HERE</h1>
  <p class="abs" style="left:62px;top:566px;width:440px;font-size:12px;line-height:14.5px;color:var(--black)">Lorem ipsum dolor sit amet, consectetuer adipiscing elit, sed diam nonummy nibh euismod tincidunt ut laoreet dolore magna aliquam erat volutpat. Ut wisi enim ad minim veniam, quis nostrud exerci tation ullamcorper suscipit lobortis nisl ut aliquip ex ea commodo consequat. Duis autem vel eum iriure dolor in</p>
  <p class="abs" style="left:66px;top:670px;font-size:10px;color:var(--black)">DEPARTMENT NAME</p>
  <div class="logo black" style="right:48px;top:657px;font-size:30px">MARROWDALE</div>
</section>

<!-- Contents -->
<section class="page contents" style="left:689px;top:98px">
  <div class="logo gold" style="left:46px;top:20px;font-size:30px">MARROWDALE</div>
  <div class="doc-label">Document Title</div>
  <h2 class="display abs" style="left:47px;top:70px;font-size:38px;font-weight:400">Contents</h2>
  <div class="abs" style="left:47px;top:124px;width:472px">
    <div class="toc-row"><span>HEADING 01</span><span class="dots"></span><span>3</span></div>
    <div class="toc-row sub"><span>HEADING 02</span><span class="dots"></span><span>3</span></div>
    <div class="toc-row"><span>BULLET LIST</span><span class="dots"></span><span>4</span></div>
    <div class="toc-row"><span>TABLE 01</span><span class="dots"></span><span>4</span></div>
    <div class="toc-row sub"><span>TABLE 02</span><span class="dots"></span><span>4</span></div>
  </div>
  <div class="footer-rule"></div>
  <p class="footer-note">The Marrowdale Institute prohibits discrimination in employment, educational programs, and activities on the basis of race, creed, color, religion, national origin, age, sex, pregnancy, disability, genetic information, status as a U.S. veteran, service in the U.S. military, sexual orientation, gender identity, associational preferences, or any other classification that deprives the person of consideration as an individual. The university also affirms its commitment to providing equal opportunities and equal access to university facilities. For additional information on nondiscrimination policies, contact the Director, Bureau of Fair Access and Inclusion, the Marrowdale Institute, 418 Penwick Hall, Harlow Falls, MN 52279-4083, 319-482-6613 (voice), 319-482-6671 (TDD), inclusion@mrwdl.edu.</p>
</section>

<!-- Text styles -->
<section class="page styles" style="left:70px;top:930px">
  <div class="logo gold" style="left:46px;top:20px;font-size:30px">MARROWDALE</div>
  <div class="doc-label">Document Title</div>
  <h2 class="display abs" style="left:46px;top:72px;font-size:34px;font-weight:400;-webkit-text-stroke:.6px #000">TITLE STYLE</h2>
  <div class="body abs" style="left:46px;top:123px;width:474px">
    <p>Lorem ipsum dolor sit amet, consectetuer adipiscing elit. Maecenas porttitor congue massa. Fusce posuere, magna sed pulvinar ultricies, purus lectus malesuada libero, sit amet commodo magna eros quis urna.</p>
    <p>Nunc viverra imperdiet enim. Fusce est. Vivamus a tellus.</p>
    <p>Pellentesque habitant morbi tristique senectus et netus et malesuada fames ac turpis egestas. Proin pharetra nonummy pede. Mauris et orci.</p>
  </div>
  <h3 class="display abs" style="left:46px;top:214px;font-size:19px;font-weight:400;-webkit-text-stroke:.4px #000">HEADING 01</h3>
  <div class="body abs" style="left:46px;top:245px;width:474px">
    <p>Lorem ipsum dolor sit amet, consectetuer adipiscing elit. Maecenas porttitor congue massa. Fusce posuere, magna sed pulvinar ultricies, purus lectus malesuada libero, sit amet commodo magna eros quis urna.</p>
    <p>Nunc viverra imperdiet enim. Fusce est. Vivamus a tellus.</p>
    <p>Pellentesque habitant morbi tristique senectus et netus et malesuada fames ac turpis egestas. Proin pharetra nonummy pede. Mauris et orci.</p>
  </div>
  <div class="abs" role="img" aria-label="Photo placeholder" style="left:353px;top:322px;width:168px;height:166px;background:var(--placeholder)"></div>
  <h4 class="display abs" style="left:46px;top:335px;font-size:13px;font-weight:400">HEADING 02</h4>
  <div class="body abs" style="left:46px;top:358px;width:300px">
    <p>Lorem ipsum dolor sit amet, consectetuer adipiscing elit. Maecenas porttitor congue massa. Fusce posuere, magna sed pulvinar ultricies, purus lectus malesuada libero, sit amet commodo magna eros quis urna.</p>
    <p>Nunc viverra imperdiet enim. Fusce est. Vivamus a tellus.</p>
    <p>Pellentesque habitant morbi tristique senectus et netus et malesuada fames ac turpis egestas. Proin pharetra nonummy pede. Mauris et orci.</p>
  </div>
  <div class="gold-band" style="left:45px;top:472px;width:302px;height:15px"></div>
  <h4 class="abs" style="left:47px;top:472px;font-size:12px;font-weight:400;color:var(--black);line-height:15px">SPECIAL TITLE</h4>
  <div class="body abs" style="left:46px;top:492px;width:474px">
    <p>Lorem ipsum dolor sit amet, consectetuer adipiscing elit. Maecenas porttitor congue massa. Fusce posuere, magna sed pulvinar ultricies, purus lectus malesuada libero, sit amet commodo magna eros quis urna.</p>
    <p>Nunc viverra imperdiet enim. Fusce est. Vivamus a tellus.</p>
    <p>Pellentesque habitant morbi tristique senectus et netus et malesuada fames ac turpis egestas. Proin pharetra nonummy pede. Mauris et orci.</p>
  </div>
  <div class="footer-rule"></div>
  <p class="footer-note">The Marrowdale Institute prohibits discrimination in employment, educational programs, and activities on the basis of race, creed, color, religion, national origin, age, sex, pregnancy, disability, genetic information, status as a U.S. veteran, service in the U.S. military, sexual orientation, gender identity, associational preferences, or any other classification that deprives the person of consideration as an individual. The university also affirms its commitment to providing equal opportunities and equal access to university facilities. For additional information on nondiscrimination policies, contact the Director, Bureau of Fair Access and Inclusion, the Marrowdale Institute, 418 Penwick Hall, Harlow Falls, MN 52279-4083, 319-482-6613 (voice), 319-482-6671 (TDD), inclusion@mrwdl.edu.</p>
</section>

<!-- Lists and tables -->
<section class="page lists" style="left:689px;top:930px">
  <div class="logo gold" style="left:46px;top:20px;font-size:30px">MARROWDALE</div>
  <div class="doc-label">Document Title</div>
  <h3 class="display abs" style="left:47px;top:68px;font-size:19px;font-weight:400;-webkit-text-stroke:.4px #000">BULLET LIST</h3>
  <ul class="bullets abs" style="left:62px;top:98px">
    <li><svg class="tick" viewBox="0 0 10 10"><circle cx="5" cy="5" r="5" fill="#fbd800"/><path d="M2.6 5.2 4.3 6.8 7.5 3.4" fill="none" stroke="#000" stroke-width="1.3"/></svg>IPN Bullet 1</li>
    <li class="l2"><span class="ring"></span>IPN Bullet 2</li>
    <li><svg class="tick" viewBox="0 0 10 10"><circle cx="5" cy="5" r="5" fill="#fbd800"/><path d="M2.6 5.2 4.3 6.8 7.5 3.4" fill="none" stroke="#000" stroke-width="1.3"/></svg>IPN Bullet 3</li>
    <li class="l2"><span class="ring"></span>IPN Bullet 4</li>
    <li><svg class="tick" viewBox="0 0 10 10"><circle cx="5" cy="5" r="5" fill="#fbd800"/><path d="M2.6 5.2 4.3 6.8 7.5 3.4" fill="none" stroke="#000" stroke-width="1.3"/></svg>IPN Bullet 5</li>
  </ul>
  <h3 class="display abs" style="left:47px;top:226px;font-size:19px;font-weight:400;-webkit-text-stroke:.4px #000">TABLE 01</h3>
  <table class="t1 abs" style="left:47px;top:259px">
    <tr><th>Name</th><th>Name</th><th>Name</th><th>Name</th><th>Name</th></tr>
    <tr><td>000</td><td>000</td><td>000</td><td>000</td><td>000</td></tr>
    <tr><td>000</td><td>000</td><td>000</td><td>000</td><td>000</td></tr>
    <tr><td>000</td><td>000</td><td>000</td><td>000</td><td>000</td></tr>
  </table>
  <p class="caption abs" style="left:47px;top:356px">Figure 1: Table 1</p>
  <h4 class="display abs" style="left:47px;top:377px;font-size:13px;font-weight:400">TABLE 02</h4>
  <table class="t2 abs" style="left:47px;top:405px">
    <tr><th>Name</th><th>Name</th><th>Name</th><th>Name</th></tr>
    <tr><td>000</td><td>000</td><td>000</td><td>000</td></tr>
    <tr><td>000</td><td>000</td><td>000</td><td>000</td></tr>
    <tr><td>000</td><td>000</td><td>000</td><td>000</td></tr>
  </table>
  <p class="caption abs" style="left:47px;top:507px">Figure 2: Table 2</p>
  <div class="abs" style="left:178px;top:545px;font-family:Georgia,serif;font-size:40px;font-weight:700;color:var(--gold);line-height:1">&ldquo;</div>
  <blockquote class="abs" style="left:204px;top:564px;width:175px;font-size:8.5px;line-height:13px;font-style:italic;color:var(--black)">Pellentesque habitant morbi tristique senectus et netus et malesuada fames ac turpis egestas. Proin pharetra nonummy pede. Mauris et orci.</blockquote>
  <div class="footer-rule"></div>
  <p class="footer-note">The Marrowdale Institute prohibits discrimination in employment, educational programs, and activities on the basis of race, creed, color, religion, national origin, age, sex, pregnancy, disability, genetic information, status as a U.S. veteran, service in the U.S. military, sexual orientation, gender identity, associational preferences, or any other classification that deprives the person of consideration as an individual. The university also affirms its commitment to providing equal opportunities and equal access to university facilities. For additional information on nondiscrimination policies, contact the Director, Bureau of Fair Access and Inclusion, the Marrowdale Institute, 418 Penwick Hall, Harlow Falls, MN 52279-4083, 319-482-6613 (voice), 319-482-6671 (TDD), inclusion@mrwdl.edu.</p>
</section>

<!-- Back cover -->
<section class="page back" style="left:353px;top:1741px">
  <div class="photo" role="img" aria-label="Photo of a campus lawn with tall trees framing a golden-domed building under a blue sky" style="left:18px;top:18px;width:529px;height:462px;background:linear-gradient(180deg,#3f82c9 0%,#9cbfe0 30%,#2f4d22 48%,#24401c 72%,#4f8f2c 85%,#5ea233 100%)"></div>
  <div class="gold-band" style="left:18px;top:480px;width:529px;height:232px"></div>
  <div class="logo black" style="right:338px;top:583px;font-size:30px">MARROWDALE</div>
  <div class="abs" style="left:243px;top:560px;width:2px;height:76px;background:var(--black)"></div>
  <p class="abs" style="left:294px;top:568px;width:210px;font-size:10px;line-height:13px;color:var(--black)">Lorem ipsum dolor sit amet, consectetuer adipiscing elit, sed diam nonummy nibh euismod tincidunt ut laoreet dolore magna aliquam erat volutpat. Ut wisi enim ad minim veniam, quis nostrud exerci tation</p>
</section>

</div>
</body>
</html>
```